Computer Security PageRoom start-up design.

Should be in Harmony with https://www.quorvane.com We need a design for our pageroom profile for our company QuorVane. We work at computer security consulting services and licensing offering a high technological DelvaShift. A Framework That Allows any security based company to analyze / monitorize / etc. really any application with high performance and stealth based on hypervisor technologies. Our main color is RED, as you will see in our logo. The design Should our deep expertise transmit / skills on security. We would like to have DelvaShift Also Represented as Lynx With an Anything That Could That remark is Iberian Lynx (if possible). Any questions are welcome :)

Industry/Entity Type

Computer Security

Requirements
Must have
• Should be in armony With https://www.quorvane.com

```html
<!DOCTYPE html>
<html lang="en">
<head>
<meta charset="utf-8">
<title>DelvaShift — PageRoom Cover</title>
<link href="https://fonts.googleapis.com/css2?family=Raleway:wght@200;300;500;600;700&family=Open+Sans:wght@400;600&display=swap" rel="stylesheet">
<style>
  :root {
    --canvas: #d4d4d4;
    --photo-light: #5a5a5a;
    --photo-dark: #1f1f20;
    --footer-bar: #2a2a2d;
    --brand-red: #e2424f;
    --brand-red-soft: #e75a66;
    --white: #ffffff;
    --icon-dark: #2b2b2e;
  }
  html, body {
    margin: 0;
    padding: 0;
    width: 1200px;
    height: 1000px;
    overflow: hidden;
    background: var(--canvas);
  }
  .cover {
    position: absolute;
    left: 202px;
    top: 273px;
    width: 826px;
    height: 314px;
    overflow: hidden;
    background: var(--photo-dark);
    font-family: "Raleway", sans-serif;
    color: var(--white);
  }
  .cover__photo {
    position: absolute;
    inset: 0;
    background:
      radial-gradient(ellipse 260px 240px at 600px 150px, var(--photo-light), transparent 75%),
      linear-gradient(90deg, #202021 0%, #2c2c2d 45%, #3b3b3c 70%, #2a2a2b 100%);
  }
  .cover__shapes {
    position: absolute;
    inset: 0;
  }
  .headline {
    position: absolute;
    left: 36px;
    top: 52px;
    margin: 0;
    font-weight: 300;
    line-height: 1;
  }
  .headline__brand {
    display: block;
    font-size: 53px;
    font-weight: 300;
    letter-spacing: 0;
    color: var(--white);
  }
  .headline__tagline {
    display: block;
    margin-top: 2px;
    font-size: 55px;
    font-weight: 200;
    letter-spacing: 0.5px;
  }
  .intro {
    position: absolute;
    left: 37px;
    top: 164px;
    margin: 0;
    font-size: 17px;
    font-weight: 500;
    line-height: 19px;
  }
  .why {
    position: absolute;
    left: 600px;
    top: 68px;
    width: 220px;
    text-align: center;
    line-height: 1;
  }
  .why__lead {
    display: block;
    font-size: 25px;
    font-weight: 300;
  }
  .why__title {
    display: block;
    font-size: 26px;
    font-weight: 700;
    margin-top: 1px;
  }
  .benefits {
    position: absolute;
    left: 624px;
    top: 132px;
    margin: 0;
    padding: 0;
    list-style: none;
  }
  .benefits__item {
    display: flex;
    align-items: center;
    height: 38px;
    font-size: 18px;
    font-weight: 600;
  }
  .benefits__icon {
    width: 22px;
    height: 22px;
    margin-right: 14px;
    flex: none;
  }
  .contact {
    position: absolute;
    left: 28px;
    top: 286px;
    display: flex;
    align-items: center;
    font-family: "Open Sans", sans-serif;
    font-style: normal;
    font-size: 13px;
    color: var(--white);
  }
  .contact__item {
    display: flex;
    align-items: center;
    margin-right: 18px;
  }
  .contact__icon {
    margin-right: 9px;
    flex: none;
  }
</style>
</head>
<body>
  <section class="cover">
    <div class="cover__photo" role="img" aria-label="Black and white photograph of an Iberian lynx over a dark network of connected nodes"></div>

    <svg class="cover__shapes" width="826" height="314" viewBox="0 0 826 314" aria-hidden="true">
      <rect class="footer-bar" x="0" y="275" width="640" height="39" fill="var(--footer-bar)"/>
      <defs>
        <linearGradient id="panelGradient" x1="0" y1="0" x2="1" y2="1">
          <stop offset="0" stop-color="var(--brand-red)"/>
          <stop offset="1" stop-color="var(--brand-red-soft)"/>
        </linearGradient>
      </defs>
      <path class="benefit-panel" d="M646 0 H826 V314 H626 L542 194 Q536 184 542 172 Z" fill="url(#panelGradient)"/>
    </svg>

    <h1 class="headline">
      <span class="headline__brand">DELVASHIFT</span>
      <span class="headline__tagline">MADE EASY</span>
    </h1>

    <p class="intro">Build your solution over the<br>solid foundation provided by<br>our top class development kit.</p>

    <div class="why">
      <span class="why__lead">WHY</span>
      <span class="why__title">CHOOSE US</span>
    </div>

    <ul class="benefits">
      <li class="benefits__item">
        <svg class="benefits__icon" viewBox="0 0 22 22" aria-hidden="true">
          <path d="M2 2 H20 V16 H14 L11 20 L8 16 H2 Z" fill="var(--icon-dark)"/>
          <path d="M6 9 L9.5 12.5 L16 6" fill="none" stroke="var(--brand-red)" stroke-width="2.4"/>
        </svg>
        Functionality
      </li>
      <li class="benefits__item">
        <svg class="benefits__icon" viewBox="0 0 22 22" aria-hidden="true">
          <g fill="var(--icon-dark)">
            <circle cx="11" cy="11" r="6.5"/>
            <rect x="9" y="1.5" width="4" height="19" rx="1"/>
            <rect x="9" y="1.5" width="4" height="19" rx="1" transform="rotate(60 11 11)"/>
            <rect x="9" y="1.5" width="4" height="19" rx="1" transform="rotate(120 11 11)"/>
          </g>
          <circle cx="11" cy="11" r="2.8" fill="var(--brand-red)"/>
        </svg>
        Ready made kit
      </li>
      <li class="benefits__item">
        <svg class="benefits__icon" viewBox="0 0 22 22" aria-hidden="true">
          <path d="M2 2 H20 V16 H8 L3 20 V16 H2 Z" fill="var(--icon-dark)"/>
          <g stroke="var(--brand-red)" stroke-width="1.8">
            <line x1="5" y1="6" x2="17" y2="6"/>
            <line x1="5" y1="9.5" x2="17" y2="9.5"/>
            <line x1="5" y1="13" x2="12" y2="13"/>
          </g>
        </svg>
        Useful Code
      </li>
    </ul>

    <address class="contact">
      <span class="contact__item">
        <svg class="contact__icon" width="18" height="12" viewBox="0 0 18 12" aria-hidden="true">
          <rect x="0.5" y="0.5" width="17" height="11" fill="var(--white)"/>
          <path d="M0.5 0.5 L9 7 L17.5 0.5" fill="none" stroke="var(--footer-bar)" stroke-width="1.3"/>
        </svg>
        info@quorvane.com
      </span>
      <span class="contact__item">
        <svg class="contact__icon" width="17" height="16" viewBox="0 0 17 16" aria-hidden="true">
          <path d="M8.5 0 L17 8 H14.5 V16 H10.5 V11 H6.5 V16 H2.5 V8 H0 Z" fill="var(--white)"/>
        </svg>
        Calle Mirador Alto 14, Bilbao, Spain
      </span>
      <span class="contact__item">
        <svg class="contact__icon" width="17" height="17" viewBox="0 0 24 24" aria-hidden="true">
          <path d="M6.6 10.8a15.1 15.1 0 0 0 6.6 6.6l2.2-2.2a1 1 0 0 1 1-.25 11.4 11.4 0 0 0 3.6.57 1 1 0 0 1 1 1V20a1 1 0 0 1-1 1A17 17 0 0 1 3 4a1 1 0 0 1 1-1h3.5a1 1 0 0 1 1 1c0 1.25.2 2.45.57 3.57a1 1 0 0 1-.25 1z" fill="var(--white)"/>
        </svg>
        +34 900 555 218
      </span>
    </address>
  </section>
</body>
</html>
```